Locksmith Store 475475 Signage

Design Brief: Locksmith Store Signage – "Locksmith 475475" [ΚΛΕΙΔΑΡΑΣ 475475 (in Greek)]
We are looking for a spectacular and professional sign design for the exterior of our locksmith store.
Signage Dimensions:
• Width: 6 meters
• Height: 1.5 meters
• Shopfront window Width: 6 meters, Height: 2.5 meters
Key Requirements (in order of importance):
1. It must be immediately clear that this is a locksmith store. [ΚΛΕΙΔΑΡΑΣ (in Greek)]
2. The store name "475475", (which is also the phone number 2310475475), should be highly visible and visually striking because this is the number that customers are calling when they are locked out.
3. The signage should also clearly communicate that except for house keys, which is obvious for a locksmith store the services we provide are:
o All kinds of house keys. ΚΛΕΙΔΙΑ ΣΠΙΤΙΩΝ(in Greek) (There is no key that we cannot do)
o Immobiliser car keys = ΚΛΕΙΔΙΑ ΑΥΤΟΚΙΝΗΤΩΝ (in Greek)
We unlock every car that exist, we program new immobilizer keys – remote controls, even if all keys are lost, we repair or change broken cells of car keys, we change batteries.
o High-security locks = ΚΛΕΙΔΑΡΙΕΣ ΑΣΦΑΛΕΙΑΣ (in Greek) we sell the best high security locks in the planet
o Armoured doors = ΠΟΡΤΕΣ ΑΣΦΑΛΕΙΑΣ (in Greek) (this may not be so important to be on the signage.
Visual Style:
We are open to creative direction, but the design should be eye-catching, professional, and modern, something that will stand out on a busy street and instantly tell customers who we are and what we offer. Also, you may use the shopfront window for graphic designs. Also, we are open if a part of the signage is digital.
________________________________________
Hello Designers,
Thank you so much for your effort and the designs you've shared.
I realized I forgot to mention that you can refer to my website at www.475475-keys.gr for more context.
Additionally, I’ve just uploaded two new photos: one showing the store with a black outline at the dimensions of the signage, and another with the large double-bit key placed in a different position to demonstrate that it is moveable.
Thanks again for your dedication!
every person that has a key

```html
<!DOCTYPE html>
<html lang="el">
<head>
<meta charset="utf-8">
<title>ΚΛΕΙΔΑΡΑΣ 475475 – Sign</title>
<link rel="stylesheet" href="https://fonts.googleapis.com/css2?family=Play:wght@400;700&display=swap">
<style>
  :root {
    --backdrop: #e6e4e0;
    --sign-navy: #0c0f2a;
    --sign-navy-edge: #05061a;
    --title-gold: #e9b52a;
    --number-white: #e8eaee;
    --label-gold: #f2b705;
    --url-white: #ffffff;
    --wood-light: #b7643a;
    --wood-dark: #6e3016;
    --edge-grey: #b9bcc4;
    --key-tone: #a8c93a;
    --steel-tone: #c9ccd2;
    --key-fade: #1a1d38;
  }
  html, body {
    margin: 0;
    width: 1200px;
    height: 900px;
    overflow: hidden;
    background: var(--backdrop);
  }
  .stage {
    position: relative;
    width: 1200px;
    height: 900px;
  }
  .shop-sign {
    position: absolute;
    left: 40px;
    top: 310px;
    width: 1120px;
    height: 280px;
    box-shadow: 0 10px 30px rgba(0,0,0,.25);
  }
  .shop-sign text {
    font-family: "Play", sans-serif;
    font-weight: 700;
  }
  .site-url { letter-spacing: 2px; }
  .service-label { letter-spacing: 1px; }
</style>
</head>
<body>
<main class="stage">
  <svg class="shop-sign" viewBox="0 0 1120 280" xmlns="http://www.w3.org/2000/svg" aria-label="ΚΛΕΙΔΑΡΑΣ 475475 sign">
    <defs>
      <linearGradient id="navyPanel" x1="0" y1="0" x2="0" y2="1">
        <stop offset="0" stop-color="var(--sign-navy)"/>
        <stop offset="1" stop-color="var(--sign-navy-edge)"/>
      </linearGradient>
      <linearGradient id="woodPanel" x1="0" y1="0" x2="1" y2="1">
        <stop offset="0" stop-color="var(--wood-light)"/>
        <stop offset="1" stop-color="var(--wood-dark)"/>
      </linearGradient>
      <linearGradient id="keyTone" x1="0" y1="0" x2="1" y2="1">
        <stop offset="0" stop-color="var(--key-tone)"/>
        <stop offset=".4" stop-color="var(--steel-tone)"/>
        <stop offset="1" stop-color="var(--key-fade)"/>
      </linearGradient>
    </defs>

    <rect class="sign-panel" width="1120" height="280" fill="url(#navyPanel)"/>

    <g class="hardware-corner" role="img" aria-label="Security lock cylinder and door bolts on a wooden door">
      <polygon points="1031,0 1120,0 1120,280 938,280" fill="url(#woodPanel)"/>
    </g>
    <polygon class="corner-edge" points="1018,0 1031,0 938,280 925,280" fill="var(--edge-grey)"/>

    <rect class="key-artwork" x="40" y="12" width="170" height="200" rx="30" fill="url(#keyTone)" opacity=".85"
          role="img" aria-label="Green-headed security key with a dimpled blade"/>

    <text class="trade-title" x="193" y="116" font-size="92" textLength="755" lengthAdjust="spacingAndGlyphs"
          fill="var(--title-gold)">ΚΛΕΙΔΑΡΑΣ</text>

    <text class="area-code" x="352" y="190" font-size="22" text-anchor="end" fill="var(--number-white)">2310</text>
    <text class="phone-number" x="364" y="194" font-size="80" textLength="472" lengthAdjust="spacingAndGlyphs"
          fill="var(--number-white)">475475</text>

    <text class="site-url" x="560" y="230" font-size="23" text-anchor="middle" fill="var(--url-white)">WWW.475475-KEYS.GR</text>

    <circle class="label-dot" cx="50" cy="254" r="9" fill="var(--label-gold)"/>
    <text class="service-label" x="70" y="262" font-size="23" textLength="285" lengthAdjust="spacingAndGlyphs"
          fill="var(--label-gold)">ΚΛΕΙΔΑΡΙΕΣ ΑΣΦΑΛΕΙΑΣ</text>

    <circle class="label-dot" cx="790" cy="256" r="9" fill="var(--label-gold)"/>
    <text class="service-label" x="808" y="264" font-size="23" textLength="286" lengthAdjust="spacingAndGlyphs"
          fill="var(--label-gold)">ΚΛΕΙΔΑΡΙΕΣ ΑΣΦΑΛΕΙΑΣ</text>
  </svg>
</main>
</body>
</html>
```